Author of female self help book in need of cover that expresses freedom and empowerment

This is the first in a series of female self help books. It is called Her Quiet Compass. The book tells my story of hitting rock bottom, winning the lottery, and discovering what I call my Quiet Compass. The purpose of the book is to help inspire women to break free from the pain of loss including divorce, job loss, or heartbreak. It will help guide a women's journey to finding their courage and motivation to move on in pursuit of happiness and joy. She will gain skills to help build resilience, tap into her inner strength, achieve success in her personal and professional life and finally create a life she loves to live.

Target Market(s)

Women 30-60 yrs, divorced, single mother, widow, working professional

Industry/Entity Type

Life Coaching

Font styles to use
Serif

Colors
fbd4d5
f59296

Requirements
Must have
• Cover must express female freedom and empowerment.
Nice to have
• I would like to see something like a mountain top scene or woman depicted with arms raised high in victory.

```html
<!DOCTYPE html>
<html lang="en">
<head>
<meta charset="utf-8">
<title>Her Quiet Compass — Book Cover</title>
<link rel="stylesheet" href="https://fonts.googleapis.com/css2?family=Noto+Serif:ital,wght@0,400;1,400;1,700&family=Passion+One:wght@400;700&display=swap">
<style>
  :root {
    --page-bg: #ffffff;
    --sky-top: #f3dbe6;
    --sky-mid: #d9a7c4;
    --tree-dark: #4a1a35;
    --field-deep: #7a2a4f;
    --field-pink: #c76b93;
    --field-light: #e3a3bd;
    --ink-dark: #1a1016;
    --text-light: #fbf7f2;
    --accent-pink: #f59296;
  }
  * { margin: 0; padding: 0; box-sizing: border-box; }
  html, body {
    width: 1200px; height: 822px; overflow: hidden;
    background: var(--page-bg);
  }
  .canvas {
    position: relative; width: 1200px; height: 822px;
  }
  .cover {
    position: absolute; left: 343px; top: 31px;
    width: 514px; height: 760px;
    overflow: hidden;
    box-shadow: 0 2px 6px rgba(0,0,0,0.25);
  }
  .cover-photo {
    position: absolute; inset: 0;
    background:
      radial-gradient(ellipse 60% 35% at 50% 20%, rgba(255,250,235,0.85), rgba(255,250,235,0) 70%),
      linear-gradient(180deg,
        var(--sky-top) 0%,
        var(--sky-mid) 28%,
        #8a4a6e 38%,
        var(--tree-dark) 48%,
        #5a1f40 62%,
        var(--field-deep) 74%,
        var(--field-pink) 88%,
        var(--field-light) 100%);
  }
  .author {
    position: absolute; left: 0; right: 0; top: 34px;
    text-align: center; color: var(--ink-dark);
    font-family: "Noto Serif", serif;
  }
  .author-name {
    font-style: italic; font-weight: 700; font-size: 24px; letter-spacing: 0.5px;
  }
  .author-role {
    font-style: italic; font-weight: 700; font-size: 13.5px; margin-top: 2px;
  }
  .lead, .tail {
    position: absolute; left: 0; right: 0;
    text-align: center; color: var(--text-light);
    font-family: "Noto Serif", serif; font-style: italic;
    font-size: 23px; line-height: 35px;
    text-shadow: 0 1px 3px rgba(0,0,0,0.4);
  }
  .lead { top: 372px; }
  .tail { top: 627px; }
  .tail .emphasis {
    font-weight: 700; font-size: 31px;
  }
  .title {
    position: absolute; left: 0; right: 0;
    text-align: center; color: var(--text-light);
    font-family: "Passion One", sans-serif; font-weight: 700;
    text-transform: uppercase; line-height: 1;
    text-shadow: 0 2px 4px rgba(40,0,20,0.55);
  }
  .title-top { top: 448px; font-size: 64px; letter-spacing: 1px; }
  .title-main { top: 515px; font-size: 92px; letter-spacing: 1px; }
  .title-main sup {
    font-size: 20px; vertical-align: top; position: relative; top: 8px;
  }
</style>
</head>
<body>
<main class="canvas">
  <article class="cover">
    <div class="cover-photo" role="img" aria-label="Photo of a woman in a field at sunset with arms raised high, trees behind her, washed in pink and purple light"></div>
    <header class="author">
      <p class="author-name">CLARA HOLT</p>
      <p class="author-role">Author, Life Strategist, Success Coach</p>
    </header>
    <p class="lead">Rock Bottom is Where She Found<br>the Keys to Unlocking</p>
    <h1>
      <span class="title title-top">Her Quiet</span>
      <span class="title title-main">Compass<sup>TM</sup></span>
    </h1>
    <p class="tail">And That Led Her on a Remarkable<br>Journey to Achieving <span class="emphasis">Success!</span></p>
  </article>
</main>
</body>
</html>
```